Flyer-Design für Konzertflyer gemischter Chor
Zielgruppe
Wir, die Klangfreunde Wellbach sind ein gemischter Chor aus der Schweiz. Für unser nächstes Konzert mit dem Titel ' Lieder zum Träumen' brauchen wir einen Flyer der auf den Anlass Aufmerksam macht.
Näheres zum Chor auf unserer Website www.klangfreunde-wellbach.ch.
Aufgabenstellung
Mit dem Titel sind nicht nur Lieder zum verlieben gemeint sondern auch Songs in die man sich verlieben kann oder die einem an etwas schönes Erinnern. Wir denken da an ein stimmungsvolles Design mit nicht nur roten Herzen.
Programmausschnitt: Winds across the silver bay , Harlan Moody / Lanterns in the rain / Kima Soro / Walk beside the quiet river tonight, Garth Wells / Paper boats at dusk, Russ Tanner / Tidal hymn, Trevor Halloway / Brightwater, Harbor lane tales / Bells over meadows , Cedar hall
Format: A5 hochkant.
Text: "Lieder zum Träumen" Konzert Klangfreunde Wellbach.
Samstag 19. November 17.00 Uhr, Uerikon/Stäfa, Singsaal Lindenhain
Sonntag 20. November 17.00Uhr, Uetikon am See, Kornblumsaal
Eintritt frei Kollekte
www.klangfreunde-wellbach.ch

```html
<!DOCTYPE html>
<html lang="de">
<head>
<meta charset="utf-8">
<title>Lieder zum Träumen – Klangfreunde Wellbach</title>
<link rel="stylesheet" href="https://fonts.googleapis.com/css2?family=Pinyon+Script&family=Roboto+Condensed:wght@300;700&family=Playfair+Display:wght@700&display=swap">
<style>
  :root {
    --paper: #ffffff;
    --ink: #111111;
    --muted: #a8a8a8;
    --night: #050505;
    --light-text: #f4f4f4;
  }
  * { margin: 0; padding: 0; box-sizing: border-box; }
  html, body { width: 846px; height: 1200px; overflow: hidden; background: var(--paper); }
  .flyer {
    position: relative;
    width: 846px;
    height: 1200px;
    overflow: hidden;
    background: var(--paper);
    font-family: "Roboto Condensed", sans-serif;
    color: var(--ink);
  }
  .portrait {
    position: absolute;
    inset: 0;
    background:
      linear-gradient(180deg, rgba(0,0,0,0) 0%, rgba(0,0,0,0) 72%, rgba(10,10,10,0.95) 80%, var(--night) 100%),
      radial-gradient(ellipse 260px 200px at 120px 480px, #3a3a3a 0%, rgba(90,90,90,0.55) 55%, rgba(255,255,255,0) 100%),
      radial-gradient(ellipse 300px 520px at 150px 420px, #cfcfcf 0%, #e9e9e9 60%, rgba(255,255,255,0) 100%),
      var(--paper);
  }
  .programme {
    position: absolute;
    top: 22px;
    left: 0;
    width: 846px;
    text-align: center;
    font-weight: 300;
    font-size: 16px;
    line-height: 28px;
    color: var(--muted);
    white-space: nowrap;
  }
  .choir {
    position: absolute;
    top: 258px;
    left: 413px;
    width: 400px;
    text-align: center;
    font-family: "Playfair Display", serif;
    font-weight: 700;
    font-size: 28px;
    line-height: 42px;
    letter-spacing: 0.5px;
  }
  .presents {
    position: absolute;
    top: 366px;
    left: 413px;
    width: 400px;
    text-align: center;
    font-size: 15px;
    font-weight: 300;
  }
  .title-word {
    position: absolute;
    font-family: "Pinyon Script", cursive;
    color: var(--ink);
    white-space: nowrap;
    line-height: 1;
  }
  .title-lieder { left: 225px; top: 420px; font-size: 180px; }
  .title-zum { left: 650px; top: 595px; font-size: 86px; transform: rotate(-6deg); transform-origin: left top; }
  .title-traeumen { left: 290px; top: 700px; font-size: 120px; }
  .dates {
    position: absolute;
    left: 36px;
    top: 1000px;
    color: var(--light-text);
  }
  .event { margin-bottom: 12px; }
  .event-when { font-weight: 700; font-size: 24px; line-height: 30px; }
  .event-where { font-weight: 300; font-size: 22px; line-height: 28px; }
  .details {
    position: absolute;
    left: 445px;
    top: 1000px;
    color: var(--light-text);
    font-weight: 700;
  }
  .admission { font-size: 29px; line-height: 34px; }
  .info-label { margin-top: 30px; margin-left: 6px; font-size: 23px; line-height: 30px; }
  .info-url { font-size: 22px; line-height: 34px; }
</style>
</head>
<body>
<main class="flyer">
  <div class="portrait" role="img" aria-label="Schwarz-weisses Porträt einer Sängerin mit zurückgelegtem Kopf und dunklem Oberteil"></div>

  <p class="programme">Winds across the silver bay, Harlan Moody / Walk beside the quiet river tonight, Garth Wells / Paper boats at dusk, Russ Tanner /<br>Tidal hymn, Trevor Halloway / Brightwater, Harbor lane tales / Bells over meadows , Cedar hall ...</p>

  <h2 class="choir">KLANGFREUNDE<br>WELLBACH</h2>
  <p class="presents">PRÄSENTIEREN LIVE:</p>

  <h1 aria-label="Lieder zum Träumen">
    <span class="title-word title-lieder">Lieder</span>
    <span class="title-word title-zum">zum</span>
    <span class="title-word title-traeumen">Träumen</span>
  </h1>

  <section class="dates">
    <div class="event">
      <p class="event-when">Samstag, 19. November, 17.00 Uhr</p>
      <p class="event-where">Uerikon/Stäfa, Singsaal Lindenhain</p>
    </div>
    <div class="event">
      <p class="event-when">Sonntag, 20. November, 17.00 Uhr</p>
      <p class="event-where">Uetikon am See, Kornblumsaal</p>
    </div>
  </section>

  <section class="details">
    <p class="admission">Eintritt frei Kollekte</p>
    <p class="info-label">Weitere Infos unter:</p>
    <p class="info-url">www.klangfreunde-wellbach.ch</p>
  </section>
</main>
</body>
</html>
```